Flyer-Design für Praxis ludova - Jenseitskontakte
Es bleibt nicht viel zu sagen: Äußerst professionell, geduldig, und alle Änderungen rasch nach meinen Wünschen durchgeführt. farbfuchs hat den Namen "Elitedesigner" absolut verdient!!!
Zielgruppe
Ich bin Medium und kann mit Verstorbenen Kontakt aufnehmen.
Aufgabenstellung
Faltblatt 6 seitig mit Wickelfalz, Format 100x210 (geöffnet A4). Folgende Daten stehen bei der Druckerei als Vorgaben:
Wickelfalz 100x210mm 6-seitig
Endformat: 297x210mm
Druckformat: 301x214mm
Beschnittzugabe: 2mm
Sicherheitsabstand: 4mm
Bitte keine verspielten, verschnörkelten Vorschläge. Es soll auf keinen Fall "abgehoben" wirken.
Die Vorderseite sollte möglichst mit dem Hintergrundbild (orange-gelb) gestaltet werden, da dies ein Teil meines Logos ist.
Die Website sollte unbedingt klar zum Ausdruck gebracht werden und auf jeden Fall auf Vorder und Rückseite klar ersichtlich sein.

```html
<!DOCTYPE html>
<html lang="de">
<head>
<meta charset="utf-8">
<title>Faltblatt ludova – Jenseitskontakte</title>
<link rel="stylesheet" href="https://fonts.googleapis.com/css2?family=Open+Sans:ital,wght@0,400;0,600;0,700;1,400;1,700;1,800&display=swap">
<style>
  :root {
    --bg: #dcdcdc;
    --paper: #ffffff;
    --orange-deep: #f07a22;
    --orange: #f7a23c;
    --yellow: #fbc96a;
    --cream-top: #fde6cf;
    --cream-bottom: #fbf0dc;
    --text: #3a3330;
    --blue: #3f6fb8;
    --blue-band: #3d6db6;
  }
  * { box-sizing: border-box; margin: 0; padding: 0; }
  html, body { width: 1200px; height: 800px; overflow: hidden; }
  body {
    background: var(--bg);
    font-family: "Open Sans", Arial, sans-serif;
    color: var(--text);
    position: relative;
  }
  .folder {
    position: absolute;
    left: 22px; top: 100px;
    display: flex; gap: 12px;
  }
  .panel {
    width: 280px; height: 600px;
    background: var(--paper);
    position: relative;
    display: flex; flex-direction: column;
    box-shadow: 0 3px 10px rgba(0,0,0,.18);
    overflow: hidden;
  }
  .panel-head {
    margin-top: 12px;
    height: 56px;
    background: linear-gradient(100deg, var(--orange-deep) 0%, var(--orange) 55%, var(--yellow) 80%, var(--orange-deep) 100%);
    display: flex; align-items: center; justify-content: center;
    color: #fff;
    font-weight: 800; font-style: italic;
    font-size: 12.5px; letter-spacing: 0;
    white-space: nowrap;
    text-align: center; padding: 0 6px;
  }
  .panel-body {
    margin-top: 6px;
    flex: 1;
    background: linear-gradient(160deg, var(--cream-top) 0%, #fef4e6 50%, var(--cream-bottom) 100%);
    padding: 14px 16px;
    font-size: 8.6px; line-height: 1.5;
  }
  .panel-body p { margin-bottom: 9px; }
  .panel-body .sub {
    color: var(--blue); font-style: italic; font-weight: 600;
    font-size: 10px; margin-bottom: 10px;
  }
  .panel-body .link {
    color: var(--blue); font-style: italic; font-weight: 700;
    font-size: 8.4px; margin: 12px 0 22px;
  }
  .photo {
    height: 200px; margin-top: 6px;
    background: linear-gradient(180deg, #c9c4bd 0%, #8a6a55 35%, #5a3b31 70%, #6d4a3c 100%);
  }
  .shop-photo {
    height: 158px;
    background: linear-gradient(180deg, #6f6863 0%, #8c7d70 55%, #4a3027 100%);
  }
  .shop-body { padding: 12px 16px 0; flex: 1; font-size: 8.4px; line-height: 1.45; }
  .shop-title {
    color: var(--orange-deep); font-weight: 700; font-style: italic;
    font-size: 14px; margin-bottom: 8px;
  }
  .product { display: flex; gap: 10px; margin-bottom: 10px; }
  .cover { width: 66px; height: 62px; flex: none; }
  .cover-orange { background: linear-gradient(135deg, #f3a44a, #e7472a); }
  .cover-violet { background: linear-gradient(135deg, #b7a7e6, #7b66c9); }
  .product-title, .book-title {
    color: var(--blue); font-weight: 700; font-style: italic; font-size: 8.6px;
    margin-bottom: 3px;
  }
  .product ol { list-style: none; }
  .book-title { margin-top: 2px; }
  .book-meta { font-style: italic; font-weight: 600; margin-top: 6px; }
  .shop-body p { margin-bottom: 6px; }
  .cta {
    background: var(--blue-band); color: #fff;
    padding: 10px 16px 12px;
  }
  .cta-title { font-style: italic; font-size: 13px; }
  .cta-text { font-size: 8.4px; }
</style>
</head>
<body>
  <main class="folder">

    <section class="panel">
      <h2 class="panel-head">Jenseitskontakte – Mediale Arbeit</h2>
      <div class="panel-body">
        <p>Die meisten von uns haben bereits einen geliebten Menschen durch den Tod verloren. Doch nach unserem physischen Tod ist es nicht vorbei, denn die Seele existiert weiter.</p>
        <p>Als Medium habe ich die Möglichkeit mit Verstorbenen zu kommunizieren und auch Beweise dafür zu erbringen.</p>
        <p>Meist öffnet eine Jenseitskontakt-Sitzung auch neue Perspektiven für das Leben oder erleichtert Phasen der Trauer – vor allem dann, wenn der Tod sehr plötzlich kam und es keinen Abschied gegeben hat.</p>
        <p>Durch die Beweise für ein Leben danach kann uns die Angst vor unserer eigenen irdischen Vergänglichkeit genommen werden.</p>
        <p>Unsere Lieben in der Geistigen Welt freuen sich, wenn sie die Möglichkeit haben, sich mitzuteilen. Einzelsitzungen nur nach Terminvereinbarung.</p>
      </div>
      <div class="photo" role="img" aria-label="Foto: Publikum bei einem medialen Vortrag im Saal"></div>
    </section>

    <section class="panel">
      <div class="shop-photo" role="img" aria-label="Foto: das Buch der Autorin auf einem Holztisch"></div>
      <div class="shop-body">
        <h2 class="shop-title">Shop</h2>
        <div class="product">
          <div class="cover cover-orange" role="img" aria-label="CD-Cover mit orangefarbener Blüte"></div>
          <div>
            <h3 class="product-title">CD „Innere Ruhe 1“</h3>
            <p>Inhalt:</p>
            <ol><li>1. Reise zum inneren Licht</li><li>2. Atem der Heilung</li><li>3. „Leere im Geist“</li></ol>
          </div>
        </div>
        <div class="product">
          <div class="cover cover-violet" role="img" aria-label="CD-Cover mit violetter Blüte"></div>
          <div>
            <h3 class="product-title">CD „Innere Ruhe 2“</h3>
            <p>Inhalt:</p>
            <ol><li>1. Ankommen im stillen Raum</li><li>2. Meditation für klare Antworten</li><li>3. Die klärende Quelle</li><li>4. Die Gabe aus dem Licht</li></ol>
          </div>
        </div>
        <h3 class="book-title">Buch „Was bleibt, wenn wir gehen?“ – Einblicke einer Hellfühlenden</h3>
        <p>Gibt es ein Leben nach dem Tod? Wenn ja, was passiert, wenn wir unseren Körper ablegen? Wie geht es Verstorbenen in der Geistigen Welt? Fragen, mit denen sich die meisten Menschen im Laufe ihres Lebens einmal beschäftigen.</p>
        <p>Die Autorin behandelt das Thema in diesem Buch aus Sicht eines Mediums und räumt dabei auch mit Missverständnissen auf. Erfahrungen aus unzähligen Jenseitskontakt-Sitzungen bilden die Grundlage, um dem Leser ein Bild über die Geistige Welt und die Kommunikation mit Verstorbenen zu vermitteln.</p>
        <p class="book-meta">Hardcover, gebunden, 196 Seiten, ISBN 978-3-900-11872-4</p>
      </div>
      <div class="cta">
        <p class="cta-title">Interesse geweckt?</p>
        <p class="cta-text">Alle Artikel können Sie bequem online unter www.ludova.at bestellen.</p>
      </div>
    </section>

    <section class="panel">
      <h2 class="panel-head">Ablauf einer medialen Einzelsitzung</h2>
      <div class="panel-body">
        <p>Nachdem Sie ein bisschen zur Ruhe gekommen sind, Ihr Handy ausgeschaltet und einfach einmal durchgeatmet haben, erkläre ich Ihnen den Ablauf der Sitzung. Ich schaue, wer sich von den Verstorbenen meldet und welche Botschaften die Geistige Welt für Sie bereithält.</p>
        <p>Bitte bedenken Sie, dass die Geistige Welt und unsere Verstorbenen niemals in unser Leben eingreifen. Der freie Wille wird ebenso respektiert wie die Tatsache, dass wir unsere Aufgaben auf unsere Weise bewältigen müssen.</p>
        <p>Sie erhalten sofort nach der Sitzung einen Mitschnitt auf CD. Antworten auf häufige Fragen zu Einzelsitzungen finden Sie auf meiner Homepage.</p>
        <p>Sitzungen finden ausschließlich als Einzelsitzungen statt, denn jeder Angehörige oder Freund hat eine eigene Beziehung zu den einzelnen Verstorbenen und so wird vermieden, dass sich jemand benachteiligt fühlt.</p>
      </div>
      <div class="photo" role="img" aria-label="Foto: Vortragssaal mit Publikum und Rednerin vor Projektion"></div>
    </section>

    <section class="panel">
      <h2 class="panel-head">Mediale Vorträge &amp; Seminare</h2>
      <div class="panel-body">
        <h3 class="sub">Vorträge:</h3>
        <p>In meinen Vorträgen erzähle ich meinen Zuhörern etwas über das Leben nach unserem irdischen Leben. Was passiert, wenn wir diese Erde und unseren Körper verlassen? Gibt es danach ein Weiterleben?</p>
        <p>Wie geht es Verstorbenen in der Geistigen Welt? Ist es möglich, Kontakt mit Verstorbenen aufzunehmen? Diese und noch andere Fragen beschäftigen viele Menschen.</p>
        <p>Mit meinen Vorträgen möchte ich Sie der Gewissheit ein Stück näher bringen, dass es nach dem physischen Tod nicht zu Ende ist. Anschließend an den Vortrag werden persönliche Botschaften von Verstorbenen an einige Besucher übermittelt.</p>
        <p class="link">Alle Vortragstermine auf www.ludova.at</p>
        <h3 class="sub">Seminare:</h3>
        <p>Die Geistige Welt ist immer bereit, mit uns zu kommunizieren! In meinen Seminaren lernen Sie mit der Geistigen Welt zu kommunizieren und Ihre medialen Fähigkeiten (die zweifellos in jedem Menschen mehr oder weniger angelegt sind) zu entdecken und zu fördern.</p>
        <p>Sie haben in jedem Seminar die Gelegenheit, sich medial zu entwickeln, Ihr "Gespür" für andere zu trainieren und gleichzeitig auch Heilung zu erfahren.</p>
        <p>Eine fundierte Ausbildung mit Zertifikat ist ebenfalls möglich.</p>
        <p class="link">Alle aktuellen Seminartermine finden Sie auf www.ludova.at</p>
      </div>
    </section>

  </main>
</body>
</html>
```